Website Design for a holiday home letting busines

We require a redesign of our present website www.birchwoodstays.com. We want the website to stand out and look professional and clean to make holiday hunters want to book a caravan or lodge holiday with us. Our logo is red however we DO NOT want the website to be red. We want a natural colour scheme.

The final design should communicate that we are a professional company to book with.

On the home page we require;
Overview of company
Photo
Search box for holiday (check in)
Late Deals
Reviews
News

We would like the following pages designed; home page, available dates page, caravans page, content page.

The website should be responsive for smart phones. One website I do like is http://www.verdamoro.be/nl/

Target Market(s)

Families

Industry/Entity Type

Travel

Number of Pages Required

5+ page

Font styles to use
Serif

Requirements
Must have
• The project must be responsive for mobile phones and tablets.
• Ability to search for holiday home holidays
• We want a natural colour scheme.
Nice to have
• A style we like is http://www.verdamoro.be/nl/
Should not have
• Do not use red as a colour for the website. Our logo is red so this is the only time we want this used.

```html
<!DOCTYPE html>
<html lang="en">
<head>
<meta charset="utf-8">
<title>Birchwood Stays – Hollowmere Castle Holidays</title>
<link href="https://fonts.googleapis.com/css2?family=Open+Sans:wght@400;600;700&display=swap" rel="stylesheet">
<style>
:root{
  --blue:#1f78c4;
  --blue-dark:#1a5f9f;
  --blue-deep:#164f86;
  --green:#8bbd3c;
  --red:#c8252c;
  --ink:#4a4a4a;
  --muted:#8a8a8a;
  --line:#dfe3e8;
  --page:#ffffff;
}
*{box-sizing:border-box;margin:0;padding:0}
html,body{width:703px;height:1200px;overflow:hidden;background:var(--page)}
body{font-family:"Open Sans",Arial,sans-serif;color:var(--ink);font-size:8px;line-height:1.45;position:relative}
.wrap{width:665px;margin:0 auto}

/* header */
.site-header{height:62px;display:flex;align-items:center;justify-content:space-between}
.brand{display:flex;align-items:center;gap:7px}
.brand-mark{width:22px;height:22px;background:var(--red);border-radius:3px}
.brand-name{color:var(--red);font-weight:700;font-size:19px;letter-spacing:-.2px}
.phone{text-align:center}
.phone small{display:block;color:var(--muted);font-size:8px}
.phone strong{color:var(--blue-dark);font-size:14px;font-weight:700}
.chat{display:flex;align-items:center;gap:6px;background:var(--green);color:#fff;border-radius:16px;padding:5px 14px 5px 6px}
.chat-dot{width:22px;height:22px;border-radius:50%;background:#fff;display:flex;align-items:center;justify-content:center}
.chat b{display:block;font-size:11px;line-height:1.1}
.chat span{font-size:7.5px}

/* nav */
.main-nav{height:22px;border-top:1px solid var(--line);border-bottom:1px solid var(--line);display:flex;align-items:center;gap:2px}
.main-nav a{color:var(--blue-dark);text-decoration:none;font-size:7px;font-weight:600;text-transform:uppercase;padding:4px 9px}
.main-nav a.active{background:var(--blue);color:#fff}

.page-title{margin-top:6px;background:var(--blue);color:#fff;font-size:13px;font-weight:700;padding:6px 12px}

/* intro */
.intro{display:flex;gap:19px;margin-top:12px}
.intro-photo{width:314px;height:240px;background:linear-gradient(160deg,#cfc9bd,#9c9386);position:relative}
.intro-caption{position:absolute;left:0;right:0;bottom:0;background:rgba(31,120,196,.88);color:#fff;font-size:7px;padding:6px 10px}
.payments{flex:1}
.payments h2{color:var(--blue);font-size:11px;font-weight:700;margin:2px 0 6px}
.payments h2+ul{margin-bottom:18px}
.ticks{list-style:none}
.ticks li{display:flex;gap:5px;align-items:center;font-size:7.5px;margin-bottom:3px}
.ticks svg{flex:none}

.copy{font-size:7.5px;margin-top:12px}
.note{margin-top:6px}
.note h3{font-size:8.5px;font-weight:700;color:var(--ink)}
.note ul{list-style:none;font-size:7.5px}
.note li::before{content:"• ";color:var(--blue)}

/* cards */
.units{display:flex;gap:12px;margin-top:10px}
.unit{width:157px;border:1px solid var(--line)}
.unit-photo{height:74px;background:linear-gradient(150deg,#d9cdb8,#9e8e76)}
.unit-title{background:var(--blue);color:#fff;padding:6px 8px;height:40px}
.unit-title b{display:block;font-size:9px}
.unit-title span{font-size:7.5px}
.unit-meta{display:flex;gap:6px;padding:6px 8px;border-bottom:1px solid var(--line);font-size:7px}
.unit-meta span{display:flex;align-items:center;gap:3px}
.unit-meta i{font-style:normal;background:#555;color:#fff;border-radius:2px;padding:0 4px}
.dates{list-style:none}
.dates li{display:flex;justify-content:space-between;align-items:center;height:46px;padding:0 8px;border-bottom:1px solid var(--line);font-size:6.5px;line-height:1.35}
.dates li:last-child{border-bottom:none}
.btn{background:var(--blue);color:#fff;font-size:6px;font-weight:700;padding:3px 6px;border-radius:2px;text-transform:uppercase}
.btn.alt{background:#6c7a86}

.pager{display:flex;justify-content:center;gap:5px;margin-top:16px}
.pager span{width:16px;height:16px;border-radius:50%;border:1px solid var(--line);display:flex;align-items:center;justify-content:center;font-size:7px;color:var(--blue)}
.pager span.on{background:var(--blue);color:#fff;border-color:var(--blue)}
.footnote{display:flex;gap:6px;align-items:flex-start;font-size:7.5px;margin-top:16px}

/* footer */
.site-footer{position:absolute;left:0;right:0;top:952px;height:248px;background:var(--blue-dark);color:#dce8f4}
.footer-cols{display:flex;gap:30px;padding-top:34px}
.footer-cols h4{color:#fff;font-size:13px;font-weight:700;text-transform:uppercase;margin-bottom:12px}
.footer-cols p{font-size:7px}
.f-news{width:200px}
.field{background:#fff;color:var(--muted);font-size:7px;padding:5px 7px;width:150px;margin-top:8px}
.subscribe{display:inline-block;background:var(--green);color:#fff;font-size:7px;font-weight:700;padding:5px 12px;margin-top:10px;text-transform:uppercase}
.f-contact{width:200px}
.f-contact p+p{margin-top:8px}
.sitemap{display:grid;grid-template-columns:90px 90px;font-size:7px;row-gap:8px}
.bottom-bar{position:absolute;left:0;right:0;bottom:0;height:28px;background:var(--blue-deep);color:#b9cde2;font-size:6.5px}
.bottom-bar .wrap{display:flex;justify-content:space-between;align-items:center;height:28px}
.social{display:flex;gap:6px;align-items:center}
.social i{width:10px;height:10px;border-radius:50%;background:#b9cde2;display:block}
</style>
</head>
<body>
<div class="wrap">
  <header class="site-header">
    <div class="brand"><div class="brand-mark"></div><span class="brand-name">Birchwood Stays</span></div>
    <div class="phone"><small>Call us today</small><strong>0800 555 0142</strong></div>
    <div class="chat">
      <div class="chat-dot"><svg width="12" height="12" viewBox="0 0 12 12"><path d="M2 2h8v6H5l-3 2z" fill="#8bbd3c"/></svg></div>
      <div><b>Questions?</b><span>Chat with us now</span></div>
    </div>
  </header>

  <nav class="main-nav">
    <a class="active">Home</a><a>News</a><a>Reviews</a><a>Caravans &amp; Lodges</a><a>Park Holidays</a><a>Late Deals</a><a>Park Facilities</a><a>Local Attractions</a><a>Contact Us</a>
  </nav>

  <h1 class="page-title">2015 Caravan and Lodge Holidays at Hollowmere Castle Holiday Park</h1>

  <section class="intro">
    <div class="intro-photo" role="img" aria-label="Photo of a caravan holiday park">
      <div class="intro-caption">Check our availability for 2015 holidays at Hollowmere Castle Holiday Park.<br>Any prices not yet filled, then ask our friendly team to check.</div>
    </div>
    <div class="payments">
      <h2>Weekly or Monthly Regular Payments</h2>
      <ul class="ticks">
        <li><svg width="8" height="8" viewBox="0 0 8 8"><path d="M1 4l2 2 4-5" stroke="#8bbd3c" stroke-width="1.5" fill="none"/></svg>Available for holidays more than 3 months away.</li>
        <li><svg width="8" height="8" viewBox="0 0 8 8"><path d="M1 4l2 2 4-5" stroke="#8bbd3c" stroke-width="1.5" fill="none"/></svg>No deposit required to book.</li>
        <li><svg width="8" height="8" viewBox="0 0 8 8"><path d="M1 4l2 2 4-5" stroke="#8bbd3c" stroke-width="1.5" fill="none"/></svg>Choose either Weekly or Monthly Payments by Direct Debit.</li>
        <li><svg width="8" height="8" viewBox="0 0 8 8"><path d="M1 4l2 2 4-5" stroke="#8bbd3c" stroke-width="1.5" fill="none"/></svg>YOU select when you want payments to come out of your bank.</li>
        <li><svg width="8" height="8" viewBox="0 0 8 8"><path d="M1 4l2 2 4-5" stroke="#8bbd3c" stroke-width="1.5" fill="none"/></svg>Payments include refundable £50 bond.</li>
      </ul>
      <h2>Weekly or Monthly Regular Payments</h2>
      <ul class="ticks">
        <li><svg width="8" height="8" viewBox="0 0 8 8"><path d="M1 4l2 2 4-5" stroke="#8bbd3c" stroke-width="1.5" fill="none"/></svg>Pay a £50 non-refundable deposit booking fee.</li>
        <li><svg width="8" height="8" viewBox="0 0 8 8"><path d="M1 4l2 2 4-5" stroke="#8bbd3c" stroke-width="1.5" fill="none"/></svg>Balance due 8 weeks before booking.</li>
        <li><svg width="8" height="8" viewBox="0 0 8 8"><path d="M1 4l2 2 4-5" stroke="#8bbd3c" stroke-width="1.5" fill="none"/></svg>Payments made either by Bank Transfer, secure online payment</li>
        <li><svg width="8" height="8" viewBox="0 0 8 8"><path d="M1 4l2 2 4-5" stroke="#8bbd3c" stroke-width="1.5" fill="none"/></svg>or over the telephone.</li>
      </ul>
    </div>
  </section>

  <p class="copy">Please note that all bookings are subject to our booking terms and conditions. Our prices do not include leisure entertainment passes. Passes are required to enter the complex, entertainment, bars, swimming and some activities. These can be purchased from the on-site reception.</p>

  <div class="note">
    <h3>Please note:</h3>
    <ul>
      <li>We do not allow pets in our caravans.</li>
      <li>Hollowmere Castle Holiday Park does not allow single sex groups.</li>
    </ul>
  </div>

  <p class="copy" style="margin-top:6px">Our prices below show 3 or 4 nights. If you are wanting a price for 7 nights please click on the price and then next page gives you an option to select 7 nights from a drop down.</p>

  <section class="units">
    <article class="unit">
      <div class="unit-photo" role="img" aria-label="Photo of the lodge interior"></div>
      <div class="unit-title"><b>The Fernbrook</b><span>(Lodge Premier)</span></div>
      <div class="unit-meta"><span>Sleeps <i>6</i></span><span>Bedrooms <i>3</i></span></div>
      <ul class="dates">
        <li><span>Fri 28 August -<br>Mon 31 August 2015</span><span class="btn">Book now</span></li>
        <li><span>Mon 31 August -<br>Fri 04 September 2015</span><span class="btn">Book now</span></li>
        <li><span>Fri 04 September -<br>Mon 07 September 2015</span><span class="btn">Book now</span></li>
        <li><span>Mon 07 September -<br>Fri 11 September 2015</span><span class="btn">Book now</span></li>
        <li><span>Fri 11 September -<br>Mon 14 September 2015</span><span class="btn">Book now</span></li>
      </ul>
    </article>
    <article class="unit">
      <div class="unit-photo" role="img" aria-label="Photo of the caravan lounge"></div>
      <div class="unit-title"><b>The Ashdale</b><span>(Gold)</span></div>
      <div class="unit-meta"><span>Sleeps <i>6</i></span><span>Bedrooms <i>3</i></span></div>
      <ul class="dates">
        <li><span>Fri 28 August -<br>Mon 31 August 2015</span><span class="btn">Book now</span></li>
        <li><span>Mon 31 August -<br>Fri 04 September 2015</span><span class="btn">Book now</span></li>
        <li><span>Fri 04 September -<br>Mon 07 September 2015</span><span class="btn">Book now</span></li>
        <li><span>Mon 07 September -<br>Fri 11 September 2015</span><span class="btn">Book now</span></li>
        <li><span>Fri 11 September -<br>Mon 14 September 2015</span><span class="btn">Book now</span></li>
      </ul>
    </article>
    <article class="unit">
      <div class="unit-photo" role="img" aria-label="Photo of the caravan living area"></div>
      <div class="unit-title"><b>The Kestrel</b><span>(Classic)</span></div>
      <div class="unit-meta"><span>Sleeps <i>6</i></span><span>Bedrooms <i>3</i></span></div>
      <ul class="dates">
        <li><span>Fri 28 August -<br>Mon 31 August 2015</span><span class="btn">Book now</span></li>
        <li><span>Mon 31 August -<br>Fri 04 September 2015</span><span class="btn alt">£279</span></li>
        <li><span>Fri 04 September -<br>Mon 07 September 2015</span><span class="btn alt">£249</span></li>
        <li><span>Mon 07 September -<br>Fri 11 September 2015</span><span class="btn">Book now</span></li>
        <li><span>Fri 11 September -<br>Mon 14 September 2015</span><span class="btn">Book now</span></li>
      </ul>
    </article>
    <article class="unit">
      <div class="unit-photo" role="img" aria-label="Photo of the caravan dining area"></div>
      <div class="unit-title"><b>The Hazelwood</b><span>(Comfort Plus)</span></div>
      <div class="unit-meta"><span>Sleeps <i>6</i></span><span>Bedrooms <i>3</i></span></div>
      <ul class="dates">
        <li><span>Fri 28 August -<br>Mon 31 August 2015</span><span class="btn">Book now</span></li>
        <li><span>Mon 31 August -<br>Fri 04 September 2015</span><span class="btn">Book now</span></li>
        <li><span>Fri 04 September -<br>Mon 07 September 2015</span><span class="btn">Book now</span></li>
        <li><span>Mon 07 September -<br>Fri 11 September 2015</span><span class="btn">Book now</span></li>
        <li><span>Fri 11 September -<br>Mon 14 September 2015</span><span class="btn">Book now</span></li>
      </ul>
    </article>
  </section>

  <div class="pager"><span>‹</span><span class="on">1</span><span>2</span><span>3</span><span>›</span></div>

  <p class="footnote"><svg width="9" height="9" viewBox="0 0 8 8"><path d="M1 4l2 2 4-5" stroke="#8bbd3c" stroke-width="1.5" fill="none"/></svg>Rows with a grey background indicate out of season holidays during these dates are advertised as quiet breaks. Please note that the pool facilities and complex are closed during this time.</p>
</div>

<footer class="site-footer">
  <div class="wrap footer-cols">
    <div class="f-news">
      <h4>Newsletter Signup</h4>
      <p>Sign up to hear about our latest offers and news.</p>
      <div class="field">Enter your Name</div>
      <div class="field">Enter your Email</div>
      <span class="subscribe">Subscribe</span>
    </div>
    <div class="f-contact">
      <h4>Contact Information</h4>
      <p>Contact our friendly team for help with bookings, availability and any questions about your stay at the park.</p>
      <p>Tel: 0800 555 0142<br>Email: hello@birchwoodstays.com</p>
    </div>
    <div>
      <h4>Sitemap</h4>
      <div class="sitemap">
        <span>About Us</span><span>Contact Us</span>
        <span>News</span><span>Reviews</span>
        <span>Blogs</span><span>Privacy Policy</span>
        <span>2015 Holidays</span><span>Booking Terms</span>
        <span>Late Deals</span><span>News</span>
        <span>Local Areas</span><span>Site Map</span>
      </div>
    </div>
  </div>
  <div class="bottom-bar">
    <div class="wrap">
      <span>Design by © 2015 Birchwood Stays. All Rights Reserved.</span>
      <div class="social">Social Icons <i></i><i></i><i></i><i></i><i></i></div>
    </div>
  </div>
</footer>
</body>
</html>
```